Vemtra Group: Business Card for a high end technology company

We need a cool new design for our business cards using our cloud logo. We are a technology consulting business. We pride ourselves on be the best of the best. We mainly focus on cloud solutions and managed services. We need a business card that sets us apart from the other technology companies in the area and allows us to stand out.

Target Market(s)

Technology departments, CIO, CEOs, and Information Technology Staff.

Industry/Entity Type

Information Technology

Contact Information for Business Card

Must have the logo and our name.
Must have employee name, email address, office phone, cell phone and website.
Need to have all info on one side a cool design on backside.

Font styles to use
Serif
Sans Serif

Requirements
Must have
• Must have the logo and our name.
• Must have employee name, email address, office phone, cell phone and website.
• Need to have all info on one side a cool design on back side.
• Must be a crisp clean design, not too busy or confusing.

```html
<!DOCTYPE html>
<html lang="en">
<head>
<meta charset="utf-8">
<title>Vemtra Group Business Card</title>
<link rel="stylesheet" href="https://fonts.googleapis.com/css2?family=Open+Sans:wght@400;600&display=swap">
<style>
  :root {
    --backdrop: #2a2d2f;
    --card-dark: #2f3032;
    --card-light: #ececec;
    --accent-blue: #2f6fd6;
    --ink-dark: #2b2b2b;
    --ink-light: #e8e8e8;
    --ink-muted: #bdbdbd;
  }
  * { margin: 0; padding: 0; box-sizing: border-box; }
  html, body { width: 1200px; height: 675px; overflow: hidden; }
  body {
    background: var(--backdrop);
    font-family: "Open Sans", sans-serif;
    position: relative;
  }
  .card {
    position: absolute;
    top: 195px;
    width: 500px;
    height: 286px;
    border-radius: 3px;
    overflow: hidden;
    box-shadow: 0 12px 30px rgba(0,0,0,0.35);
  }

  /* Front side */
  .card-front { left: 70px; background: var(--card-dark); display: flex; }
  .front-brand {
    width: 176px;
    background: var(--card-light);
    display: flex;
    flex-direction: column;
    align-items: center;
    justify-content: center;
    gap: 8px;
  }
  .brand-name-row { display: flex; align-items: center; gap: 6px; }
  .brand-dot { width: 12px; height: 12px; border-radius: 50%; background: var(--accent-blue); }
  .brand-name { font-size: 21px; font-weight: 400; color: var(--ink-dark); }
  .brand-web { font-size: 8px; font-weight: 600; color: var(--ink-dark); }
  .front-accent { width: 6px; background: var(--accent-blue); }
  .front-details { flex: 1; padding: 40px 0 0 26px; color: var(--ink-light); }
  .person-name { font-size: 21px; font-weight: 400; letter-spacing: 0.3px; }
  .person-title { font-size: 10px; color: var(--ink-muted); margin-top: 2px; }
  .name-rule { width: 88px; height: 1.5px; background: var(--ink-light); margin: 8px 0 28px; }
  .contact-list { list-style: none; display: flex; flex-direction: column; gap: 9px; }
  .contact-item { display: flex; align-items: center; gap: 7px; font-size: 10px; color: var(--ink-light); }
  .contact-icon { width: 12px; height: 12px; flex: none; }

  /* Back side */
  .card-back { left: 630px; background: var(--card-dark); }
  .back-band {
    position: absolute;
    left: 0; right: 0;
    top: 78px;
    height: 124px;
    background: var(--card-light);
    display: flex;
    flex-direction: column;
    align-items: center;
    justify-content: center;
    gap: 6px;
  }
  .card-back .brand-name { font-size: 26px; }
  .card-back .brand-dot { width: 15px; height: 15px; }
  .card-back .brand-web { font-size: 9px; }
</style>
</head>
<body>
  <section class="card card-front">
    <div class="front-brand">
      <div class="brand-name-row">
        <span class="brand-dot"></span>
        <span class="brand-name">Vemtra Group</span>
      </div>
      <span class="brand-web">www.vemtragroup.com</span>
    </div>
    <div class="front-accent"></div>
    <div class="front-details">
      <h1 class="person-name">Your Name Here</h1>
      <p class="person-title">Tittle here</p>
      <div class="name-rule"></div>
      <ul class="contact-list">
        <li class="contact-item">
          <svg class="contact-icon" viewBox="0 0 12 12" fill="none" stroke="currentColor" stroke-width="0.8"><circle cx="6" cy="6" r="5.4"/><rect x="4.3" y="3" width="3.4" height="6" rx="0.6"/></svg>
          Cellphone
        </li>
        <li class="contact-item">
          <svg class="contact-icon" viewBox="0 0 12 12" fill="none" stroke="currentColor" stroke-width="0.8"><circle cx="6" cy="6" r="5.4"/><path d="M4 3.5c0 2.5 2 4.5 4.5 4.5l0.5-1-1.2-0.7-0.6 0.5c-0.8-0.4-1.4-1-1.8-1.8l0.5-0.6L5.2 3.2z"/></svg>
          Company phone
        </li>
        <li class="contact-item">
          <svg class="contact-icon" viewBox="0 0 12 12" fill="none" stroke="currentColor" stroke-width="0.8"><circle cx="6" cy="6" r="5.4"/><rect x="3.2" y="4" width="5.6" height="4" rx="0.4"/><path d="M3.2 4.2 6 6.3l2.8-2.1"/></svg>
          youremail@mailbox.com
        </li>
        <li class="contact-item">
          <svg class="contact-icon" viewBox="0 0 12 12" fill="none" stroke="currentColor" stroke-width="0.8"><circle cx="6" cy="6" r="5.4"/><circle cx="6" cy="6" r="2.8"/><path d="M3.2 6h5.6M6 3.2c-1.2 1.5-1.2 4.1 0 5.6M6 3.2c1.2 1.5 1.2 4.1 0 5.6"/></svg>
          www.yourwebsite.com
        </li>
      </ul>
    </div>
  </section>

  <section class="card card-back">
    <div class="back-band">
      <div class="brand-name-row">
        <span class="brand-dot"></span>
        <span class="brand-name">Vemtra Group</span>
      </div>
      <span class="brand-web">www.vemtragroup.com</span>
    </div>
  </section>
</body>
</html>
```